Business Card Design for Small Electrical Contractor

I need to update my business card into something a little more modern. We are a small electrical contracting company. We service domestic and commercial places around Sydney. We have 2 logo designs at the moment. I have uploaded both and 2 different sizes to work with.

Industry/Entity Type

Business

Contact Information for Business Card

Ted Corbin
8/21-23 Holt St, Fernhaven 2087
t - (02) 9471 3820
m - 0427 915 304
E - info@corbinelec.example.au
W - corbinelec.example.au
ABN: 42 907 518 263

Font styles to use
Sans Serif

Requirements
Must have
• I would also like to see the below fit on somewhere aswell
• - Licensed Electrician
• - Level 2 (Cat 1 & 4)
• - Domestic
• - Commercial
• - Repairs and Installations
• - Data
Nice to have
• Try and keep similar colours as logo
Should not have
• No lightning bolts or light globes. Smart and professional please.

```html
<!DOCTYPE html>
<html lang="en">
<head>
<meta charset="utf-8">
<title>T&amp;C Corbin Electrical – Business Card</title>
<link href="https://fonts.googleapis.com/css2?family=Arimo:wght@400;700&display=swap" rel="stylesheet">
<style>
  :root {
    --ink: #0b0b0b;
    --paper: #ffffff;
    --orange: #f0861c;
    --text-dark: #2a2a2a;
    --backdrop: #dcd8d2;
  }
  * { box-sizing: border-box; margin: 0; padding: 0; }
  html, body {
    width: 1200px; height: 843px; overflow: hidden;
    background: var(--backdrop);
    font-family: "Arimo", Arial, sans-serif;
  }
  .stage {
    width: 1200px; height: 843px;
    display: flex; align-items: center; justify-content: center; gap: 48px;
  }
  .card {
    width: 530px; height: 324px; position: relative;
    box-shadow: 0 6px 18px rgba(0,0,0,.18);
  }
  /* Front */
  .card--front { background: var(--ink); color: var(--orange); }
  .brand {
    position: absolute; top: 42px; right: 40px; text-align: right;
  }
  .brand__name {
    color: var(--paper); font-weight: 700; font-size: 30px; letter-spacing: .5px;
    display: flex; align-items: center; gap: 10px; justify-content: flex-end;
  }
  .brand__mark { width: 14px; height: 14px; border-radius: 50%; background: var(--orange); }
  .brand__est { color: var(--paper); font-size: 13px; font-weight: 700; margin-top: 4px; }
  .brand__rule { height: 2px; background: var(--orange); width: 260px; margin: 6px 0 0 auto; }
  .abn { font-size: 13px; margin-top: 8px; letter-spacing: .5px; }
  .abn b { font-weight: 700; }
  .services {
    position: absolute; left: 40px; bottom: 34px; list-style: none;
    font-size: 16px; line-height: 1.75;
  }
  .services li::before { content: "•"; margin-right: 8px; }
  .services .dot { margin: 0 8px; }
  /* Back */
  .card--back { background: var(--paper); color: var(--text-dark); padding: 56px 0 0 52px; }
  .person {
    color: var(--orange); font-weight: 700; font-size: 23px; text-transform: uppercase; letter-spacing: .5px;
  }
  .person__rule { width: 92px; height: 2px; background: var(--ink); margin: 12px 0 16px; }
  .contacts { list-style: none; font-size: 16px; line-height: 1.5; }
  .contacts li { display: flex; align-items: flex-start; gap: 12px; }
  .contacts svg { width: 15px; height: 15px; flex: none; margin-top: 3px; fill: var(--orange); }
  .contacts .group { margin-bottom: 8px; }
</style>
</head>
<body>
<main class="stage">
  <section class="card card--front" aria-label="Card front">
    <div class="brand">
      <div class="brand__name"><span class="brand__mark"></span>T&amp;C Corbin Electrical</div>
      <div class="brand__est">Est. 1980</div>
      <div class="brand__rule"></div>
      <p class="abn"><b>ABN:</b> 42 907 518 263</p>
    </div>
    <ul class="services">
      <li>Licensed Electrician</li>
      <li>Level 2 (Cat 1 &amp; 4)</li>
      <li>Domestic<span class="dot">•</span>Commercial</li>
      <li>Repairs and Installations<span class="dot">•</span>Data</li>
    </ul>
  </section>

  <section class="card card--back" aria-label="Card back">
    <h1 class="person">Ted Corbin</h1>
    <div class="person__rule"></div>
    <ul class="contacts">
      <li class="group">
        <svg viewBox="0 0 16 16" aria-hidden="true"><path d="M8 0a5.5 5.5 0 0 0-5.5 5.5C2.5 10 8 16 8 16s5.5-6 5.5-10.5A5.5 5.5 0 0 0 8 0zm0 7.8a2.3 2.3 0 1 1 0-4.6 2.3 2.3 0 0 1 0 4.6z"/></svg>
        <span>8/21-23 Holt St<br>Fernhaven 2087</span>
      </li>
      <li>
        <svg viewBox="0 0 16 16" aria-hidden="true"><path d="M1 5c2-3 12-3 14 0v2h-4V5.5H5V7H1zM3 8h10l1 6H2z"/></svg>
        <span>(02) 9471 3820</span>
      </li>
      <li>
        <svg viewBox="0 0 16 16" aria-hidden="true"><path d="M4 0h8a1 1 0 0 1 1 1v14a1 1 0 0 1-1 1H4a1 1 0 0 1-1-1V1a1 1 0 0 1 1-1zm1 2v10h6V2zm3 11a1 1 0 1 0 0 2 1 1 0 0 0 0-2z"/></svg>
        <span>0427 915 304</span>
      </li>
      <li>
        <svg viewBox="0 0 16 16" aria-hidden="true"><path d="M1 3h14v10H1zm1.5 1.5L8 9l5.5-4.5z"/></svg>
        <span>info@corbinelec.example.au</span>
      </li>
      <li>
        <svg viewBox="0 0 16 16" aria-hidden="true"><path d="M8 0a8 8 0 1 0 0 16A8 8 0 0 0 8 0zm0 2a6 6 0 0 1 5.7 4H10L8 4 6 6l2 2-1 3 2 3a6 6 0 0 1-1 0A6 6 0 0 1 8 2z"/></svg>
        <span>www.corbinelec.example.au</span>
      </li>
    </ul>
  </section>
</main>
</body>
</html>
```